Architecture firm needing a business card

We need a business card design for a new company based in the US called "Pellmore Architecture". Seeking minimalist designs that have a creativity/design feel but must be clean and professional. Please refer to the logo attached.

Target Market(s)

Real Estate Investors, Home Builders and Construction Firms.

Industry/Entity Type

Architecture

Contact Information for Business Card

Standard US size business cards. Would like to have some sort of graphic on the back side of the card - nothing that is too loud but something that may catch your attention. More or less grayscale colors that are in line with the logo colors (navy and greys essentially). Additional colors maybe accepted if blended properly (earthtones), but might be difficult to accomplish and maintain the clean/minimalist look.

Requirements
Must have
• Clean Lines
Nice to have
• some sort of graphics, would like to have something creative on the back side of the card
Should not have
• nothing too busy, cluttered or overwhelming.

```html
<!DOCTYPE html>
<html lang="en">
<head>
<meta charset="utf-8">
<title>Pellmore Architecture – Business Card</title>
<link href="https://fonts.googleapis.com/css2?family=Source+Sans+3:wght@400;600&display=swap" rel="stylesheet">
<style>
  :root {
    --navy: #1c426b;
    --grey: #9a9a9a;
    --paper: #ffffff;
    --backdrop: #e4e5e6;
    --ink-light: #ffffff;
  }
  * { box-sizing: border-box; margin: 0; padding: 0; }
  html, body {
    width: 1200px; height: 900px; overflow: hidden;
    background: var(--backdrop);
    font-family: "Source Sans 3", Arial, sans-serif;
  }
  .canvas { position: relative; width: 1200px; height: 900px; }

  .card {
    position: absolute;
    width: 560px; height: 320px;
    background: var(--paper);
    box-shadow: 0 2px 6px rgba(0,0,0,0.12);
    overflow: hidden;
  }

  /* Front */
  .card--front { left: 560px; top: 90px; }
  .brand {
    position: absolute; left: 0; right: 0; top: 50%;
    transform: translateY(-50%);
    display: flex; align-items: center; justify-content: center; gap: 20px;
  }
  .brand__square { width: 64px; height: 64px; background: var(--navy); flex: none; }
  .brand__words {
    display: flex; flex-direction: column;
    color: var(--navy); font-weight: 400; text-transform: uppercase; line-height: 1;
  }
  .brand__name { font-size: 44px; letter-spacing: 3px; }
  .brand__line { font-size: 18px; letter-spacing: 7px; margin-top: 6px; }

  /* Back */
  .card--back { left: 90px; top: 470px; display: flex; }
  .card__mark {
    width: 46%; height: 100%;
    display: flex; flex-direction: column; justify-content: center; align-items: center; gap: 16px;
  }
  .card__mark .brand__square { width: 110px; height: 110px; }
  .card__mark .brand__name { font-size: 22px; letter-spacing: 2px; color: var(--navy); text-transform: uppercase; }
  .card__info {
    width: 54%; height: 100%;
    background: var(--navy); color: var(--ink-light);
    padding: 34px 28px 0 20px; text-align: right;
  }
  .person__name { font-weight: 600; font-size: 19px; line-height: 1.1; }
  .person__role { font-size: 15px; line-height: 1.2; }
  .address { margin-top: 16px; font-size: 16px; line-height: 1.25; }
  .contacts { margin-top: 22px; list-style: none; font-size: 16px; line-height: 1.3; }
  .contacts li { display: flex; justify-content: flex-end; align-items: center; gap: 8px; }
  .contacts svg { width: 12px; height: 12px; flex: none; }
</style>
</head>
<body>
<main class="canvas">
  <section class="card card--front" aria-label="Card front">
    <div class="brand">
      <span class="brand__square"></span>
      <span class="brand__words">
        <span class="brand__name">Pellmore</span>
        <span class="brand__line">Architecture</span>
      </span>
    </div>
  </section>

  <section class="card card--back" aria-label="Card back">
    <div class="card__mark">
      <span class="brand__square"></span>
      <span class="brand__name">Pellmore</span>
    </div>
    <div class="card__info">
      <p class="person__name">Daniel Reyes</p>
      <p class="person__role">Managing Director</p>
      <p class="address">2480, Linden Avenue<br>Portland OR, 97205.</p>
      <ul class="contacts">
        <li>503-555 014 822
          <svg viewBox="0 0 12 12" aria-hidden="true"><path d="M2 4 Q6 0 10 4 L9 5.5 L7.5 4.5 L4.5 4.5 L3 5.5 Z M3 7 H9 V10 H3 Z" fill="#fff"/></svg>
        </li>
        <li>info@pellmore.com
          <svg viewBox="0 0 12 12" aria-hidden="true"><rect x="1" y="3" width="10" height="7" fill="#fff"/><path d="M1 3 L6 7 L11 3" fill="none" stroke="#1c426b" stroke-width="1"/></svg>
        </li>
        <li>www.pellmore.com
          <svg viewBox="0 0 12 12" aria-hidden="true"><path d="M5 7 L7 5 M4 6 L2.5 7.5 a1.6 1.6 0 0 0 2 2 L6 8 M8 6 L9.5 4.5 a1.6 1.6 0 0 0 -2 -2 L6 4" fill="none" stroke="#fff" stroke-width="1.2"/></svg>
        </li>
      </ul>
    </div>
  </section>
</main>
</body>
</html>
```